Solar appointment reminder card

We are looking for a new design for our appointment reminder card since we have changed our logo. The card should have the new logo along with space for the employee to hand write the customers appointment date, time, the employees name and phone number.
I've uploaded what our old basic appointment card looked like and our new logo.

The cards should be in a standard business card size and could be horizontal or vertical.

```html
<!DOCTYPE html>
<html lang="en">
<head>
<meta charset="utf-8">
<title>Appointment Reminder Card</title>
<link href="https://fonts.googleapis.com/css2?family=Montserrat:wght@700;800&display=swap" rel="stylesheet">
<style>
  :root {
    --page-bg: #e8edf1;
    --card-bg: #ffffff;
    --band-orange-top: #d97a14;
    --band-orange-bottom: #f7931e;
    --band-grey: #8c8c8c;
    --brand-orange: #f08a16;
    --title-yellow: #f6b51e;
    --label-grey: #7a7a7a;
    --rule-grey: #9a9a9a;
    --watermark-grey: rgba(200, 200, 200, 0.35);
    --watermark-sun: rgba(252, 214, 120, 0.35);
  }
  html, body {
    margin: 0;
    padding: 0;
    width: 768px;
    height: 1200px;
    overflow: hidden;
    background: var(--page-bg);
    font-family: "Montserrat", Arial, sans-serif;
  }
  .card {
    position: absolute;
    left: 34px;
    top: 400px;
    width: 700px;
    height: 400px;
    background: var(--card-bg);
    box-shadow: 0 2px 6px rgba(0, 0, 0, 0.25);
    overflow: hidden;
  }
  .side-band {
    position: absolute;
    left: 16px;
    top: 0;
    width: 80px;
    height: 340px;
    background: linear-gradient(to bottom, var(--band-orange-top), var(--band-orange-bottom));
  }
  .side-band-foot {
    position: absolute;
    left: 16px;
    top: 348px;
    width: 80px;
    height: 52px;
    background: var(--band-grey);
  }
  .brand-disc {
    position: absolute;
    left: 36px;
    top: 28px;
    width: 150px;
    height: 150px;
    border-radius: 50%;
    background: var(--card-bg);
  }
  .brand-name {
    position: absolute;
    left: 80px;
    top: 66px;
    margin: 0;
    font-size: 52px;
    font-weight: 800;
    letter-spacing: -1px;
    color: var(--brand-orange);
  }
  .landmark-watermark {
    position: absolute;
    left: 352px;
    top: 10px;
    width: 190px;
    height: 390px;
    background: linear-gradient(to bottom, var(--watermark-grey), rgba(220, 220, 220, 0.2));
    border-radius: 40px 40px 0 0;
  }
  .sun-watermark {
    position: absolute;
    right: -120px;
    top: 30px;
    width: 300px;
    height: 360px;
    background: radial-gradient(circle at 60% 50%, var(--watermark-sun) 0%, rgba(252, 214, 120, 0.15) 55%, rgba(255, 255, 255, 0) 72%);
  }
  .card-title {
    position: absolute;
    left: 338px;
    top: 74px;
    margin: 0;
    font-size: 35px;
    font-weight: 800;
    color: var(--title-yellow);
    letter-spacing: 0.5px;
  }
  .appointment-fields {
    position: absolute;
    left: 162px;
    top: 184px;
    width: 460px;
    margin: 0;
    padding: 0;
    list-style: none;
  }
  .field {
    display: flex;
    align-items: baseline;
    height: 37px;
    font-size: 17px;
    font-weight: 700;
    color: var(--label-grey);
  }
  .field-line {
    flex: 1;
    margin-left: 12px;
    border-bottom: 1px dotted var(--rule-grey);
  }
</style>
</head>
<body>
  <section class="card" aria-label="Appointment reminder card">
    <div class="landmark-watermark" role="img" aria-label="Faint statue landmark silhouette watermark"></div>
    <div class="sun-watermark" role="img" aria-label="Faint warm sun glow decoration"></div>
    <div class="side-band"></div>
    <div class="side-band-foot"></div>
    <div class="brand-disc"></div>
    <h1 class="brand-name">HRSP</h1>
    <h2 class="card-title">APPOINTMENT</h2>
    <ul class="appointment-fields">
      <li class="field"><span class="field-label">DATE:</span><span class="field-line"></span></li>
      <li class="field"><span class="field-label">TIME:</span><span class="field-line"></span></li>
      <li class="field"><span class="field-label">REPRESENTATIVE:</span><span class="field-line"></span></li>
      <li class="field"><span class="field-label">PHONE NUMBER:</span><span class="field-line"></span></li>
    </ul>
  </section>
</body>
</html>
```